Postcard Coupon Design

Local bar "The Mossy" we have great food, BBQ, wings, burgers, I would like to incorporate on the back company information such as happy hours, food specials,
and on the front a nice BBQ picture with some wings, and the following offers
"Free wings with any pitcher of regular priced beer"
"$5 off any check of $25 or more"
"Buy one get one free sandwiches 11am-3pm"
"Buy one get one free Appetizers"
The following on the back
"One coupon per customer per day, not to be combined with any other offers"
Check us out on Tapsheetly.com
www.themossy.com
happy hour 4-6pm M-F all beers and mixed drinks on special!
610-482-7319
218 Kelling Avenue
Phoenixville, PA 19460

Industry/Entity Type

It Company

Font styles to use
Serif
Sans Serif

Colors

Designer to choose colors to be used in the design.

```html
<!DOCTYPE html>
<html lang="en">
<head>
<meta charset="utf-8">
<title>The Mossy – Lunch Coupons</title>
<link href="https://fonts.googleapis.com/css2?family=PT+Sans:wght@400;700&family=PT+Serif:wght@400&display=swap" rel="stylesheet">
<style>
  :root {
    --bg: #151515;
    --logo-bg: #000000;
    --gold: #e9a322;
    --paper: #ffffff;
    --ink: #1c1c1c;
    --green: #2e8b3a;
    --red: #a3231f;
    --yellow: #f2b533;
    --dash: #6b6b6b;
  }
  html, body {
    margin: 0;
    padding: 0;
    overflow: hidden;
    background: #2a2a2a;
  }
  .postcard {
    position: relative;
    width: 1200px;
    height: 929px;
    background: var(--bg);
    overflow: hidden;
    font-family: "PT Sans", Arial, sans-serif;
  }
  .tagline {
    position: absolute;
    color: var(--gold);
    font-size: 42px;
    line-height: 1.12;
    text-align: center;
    margin: 0;
  }
  .tagline--left { left: 20px; top: 50px; width: 420px; }
  .tagline--right { right: 20px; top: 50px; width: 400px; }

  .brand {
    position: absolute;
    left: 440px;
    top: 0;
    width: 360px;
    height: 268px;
    background: var(--logo-bg);
    display: flex;
    align-items: center;
    justify-content: center;
    gap: 18px;
  }
  .brand__dot {
    width: 22px;
    height: 22px;
    border-radius: 50%;
    background: var(--gold);
  }
  .brand__name {
    color: var(--gold);
    font-size: 64px;
    font-weight: 700;
  }

  .offers {
    position: absolute;
    left: 0;
    top: 283px;
    width: 1200px;
    height: 318px;
    background: var(--paper);
  }
  .coupon {
    position: absolute;
    top: 14px;
    height: 288px;
    border: 2px dashed var(--dash);
    box-sizing: border-box;
    text-align: center;
    color: var(--ink);
    display: flex;
    flex-direction: column;
    align-items: center;
    padding-top: 22px;
  }
  .coupon--sandwich { left: 26px; width: 282px; }
  .coupon--check { left: 310px; width: 284px; }
  .coupon--appetizer { left: 596px; width: 284px; }
  .coupon--wings { left: 882px; width: 290px; }

  .coupon__lead { font-size: 31px; line-height: 1.15; margin: 0; }
  .coupon__big { font-size: 64px; line-height: 1.05; margin: 6px 0 2px; }
  .coupon__big--green { color: var(--green); }
  .coupon__big--red { color: var(--red); font-family: "PT Serif", Georgia, serif; }
  .coupon__big--ink { color: var(--ink); }
  .coupon__big--yellow { color: var(--yellow); }
  .coupon__detail { font-size: 31px; line-height: 1.15; margin: 0; }
  .coupon__hours { font-size: 22px; margin: 4px 0 0; }
  .coupon__terms {
    position: absolute;
    bottom: 14px;
    left: 0;
    right: 0;
    font-size: 12px;
    line-height: 1.3;
    margin: 0;
  }

  .photo {
    position: absolute;
    top: 612px;
    height: 305px;
  }
  .photo--brisket {
    left: 16px; width: 372px;
    background: radial-gradient(ellipse at 50% 55%, #7a3020 0%, #4a1a12 45%, #2a1410 100%);
  }
  .photo--pulled-pork {
    left: 404px; width: 396px;
    background: radial-gradient(ellipse at 50% 50%, #b0806a 0%, #7a4a35 45%, #3f2a1c 100%);
  }
  .photo--wings {
    left: 816px; width: 370px;
    background: radial-gradient(ellipse at 50% 50%, #8a3a18 0%, #5a1e10 50%, #9a1a14 100%);
  }
</style>
</head>
<body>
<div class="postcard">
  <p class="tagline tagline--left">Great BBQ,<br>wings<br>and burgers!</p>

  <div class="brand">
    <span class="brand__dot"></span>
    <span class="brand__name">The Mossy</span>
  </div>

  <p class="tagline tagline--right">Come join<br>us for lunch!</p>

  <section class="offers">
    <div class="coupon coupon--sandwich">
      <p class="coupon__lead">Buy one get one</p>
      <p class="coupon__big coupon__big--green">FREE</p>
      <p class="coupon__detail">sandwiches</p>
      <p class="coupon__hours">11am - 3pm</p>
      <p class="coupon__terms">One coupon per customer per day<br>Not to be combined with any other offers</p>
    </div>

    <div class="coupon coupon--check">
      <p class="coupon__big coupon__big--red">$5 off</p>
      <p class="coupon__detail">with check of<br>$25 or more</p>
      <p class="coupon__terms">One coupon per customer per day<br>Not to be combined with any other offers</p>
    </div>

    <div class="coupon coupon--appetizer">
      <p class="coupon__lead">Buy one get one</p>
      <p class="coupon__big coupon__big--ink">FREE</p>
      <p class="coupon__detail">Appetizers</p>
      <p class="coupon__terms">One coupon per customer per day<br>Not to be combined with any other offers</p>
    </div>

    <div class="coupon coupon--wings">
      <p class="coupon__big coupon__big--yellow">FREE</p>
      <p class="coupon__detail">wings with any<br>pitcher of<br>regular priced beer</p>
      <p class="coupon__terms">One coupon per customer per day<br>Not to be combined with any other offers</p>
    </div>
  </section>

  <div class="photo photo--brisket" role="img" aria-label="Photo of sliced smoked BBQ brisket with a dark bark"></div>
  <div class="photo photo--pulled-pork" role="img" aria-label="Photo of a pile of smoked pulled pork"></div>
  <div class="photo photo--wings" role="img" aria-label="Photo of glazed BBQ chicken wings on a red plate"></div>
</div>
</body>
</html>
```